Vent doux

Hello,
I’m a designer sunglasses reatail Store owner in Montreal, Quebec.

Looking for something modern, fresh with a trendy appeal.

Will send my logo.
Thank you.

Store

```html
<!DOCTYPE html>
<html lang="fr">
<head>
<meta charset="utf-8">
<title>Vent doux – cartes d'affaires</title>
<link rel="stylesheet" href="https://fonts.googleapis.com/css2?family=Didact+Gothic&display=swap">
<style>
  :root {
    --bg: #141414;
    --card-dark: #2a2a2c;
    --card-dark-edge: #1c1c1d;
    --card-black: #1a1a1a;
    --paper: #ececec;
    --accent: #c8244a;
    --ink-light: #f2f2f2;
    --ink-dark: #333333;
    --ink-muted: #bdbdbd;
  }
  * { margin: 0; padding: 0; box-sizing: border-box; }
  html, body { width: 1200px; height: 900px; overflow: hidden; background: var(--bg); }
  body { font-family: "Didact Gothic", "Century Gothic", sans-serif; position: relative; }

  .card {
    position: absolute;
    top: 100px;
    width: 420px;
    height: 700px;
    border-radius: 34px;
    overflow: hidden;
    box-shadow: 0 18px 40px rgba(0,0,0,.6);
  }
  .card--front { left: 160px; background: radial-gradient(ellipse at 50% 55%, var(--card-dark), var(--card-dark-edge)); }
  .card--back { left: 620px; background: var(--card-black); display: flex; align-items: center; justify-content: center; }

  .front-wave { position: absolute; top: 0; left: 0; width: 420px; height: 360px; }

  .brand { position: absolute; left: 0; width: 100%; text-align: center; }
  .card--front .brand { top: 110px; }
  .brand-row { display: flex; align-items: center; justify-content: center; gap: 12px; }
  .brand-dot { width: 30px; height: 30px; border-radius: 50%; background: var(--accent); }
  .brand-name { font-size: 40px; letter-spacing: 3px; color: var(--ink-dark); text-transform: uppercase; }
  .brand-rule { width: 250px; height: 2px; background: var(--accent); margin: 8px auto 6px; }
  .brand-tagline { font-size: 17px; letter-spacing: 3px; color: var(--ink-dark); }
  .card--back .brand { position: static; }
  .card--back .brand-name, .card--back .brand-tagline { color: var(--ink-light); }

  .details { position: absolute; top: 385px; left: 0; width: 100%; text-align: center; color: var(--ink-light); }
  .person-name { font-size: 26px; letter-spacing: 1px; }
  .person-role { font-size: 17px; color: var(--ink-muted); margin-top: 2px; }
  .contact-list { list-style: none; margin-top: 30px; font-size: 18px; }
  .contact-list li { display: flex; align-items: center; justify-content: center; gap: 10px; margin-bottom: 10px; }
  .contact-icon { width: 22px; height: 22px; }
  .address { margin-top: 22px; font-size: 18px; line-height: 1.5; }
</style>
</head>
<body>

<section class="card card--front">
  <svg class="front-wave" viewBox="0 0 420 360" aria-hidden="true">
    <path fill="var(--accent)" d="M0,0 H420 V214 C420,288 380,318 328,308 C276,298 252,248 210,258 C168,268 158,340 98,340 C36,340 0,318 0,276 Z"/>
    <path fill="var(--paper)" d="M0,0 H420 V196 C420,270 380,300 328,290 C276,280 252,230 210,240 C168,250 158,322 98,322 C36,322 0,300 0,258 Z"/>
  </svg>
  <div class="brand">
    <div class="brand-row"><span class="brand-dot"></span><span class="brand-name">Vent doux</span></div>
    <div class="brand-rule"></div>
    <div class="brand-tagline">lunettes &amp; accessoires</div>
  </div>

  <div class="details">
    <div class="person-name">MARC DELORME</div>
    <div class="person-role">Managing Director</div>
    <ul class="contact-list">
      <li>
        <svg class="contact-icon" viewBox="0 0 24 24"><circle cx="12" cy="12" r="11" fill="var(--ink-light)"/><path d="M8 7c1-1 2 0 2.6 1.4.4.8 0 1.3-.5 1.8.6 1.4 1.6 2.5 3 3.1.5-.5 1-.9 1.8-.5 1.4.6 2.4 1.6 1.4 2.6-1.6 1.6-4.5.6-6.6-1.5S6.4 8.6 8 7z" fill="var(--card-dark)"/></svg>
        514 555-0142
      </li>
      <li>
        <svg class="contact-icon" viewBox="0 0 24 24"><circle cx="12" cy="12" r="11" fill="var(--ink-light)"/><rect x="6" y="8" width="12" height="8" fill="none" stroke="var(--card-dark)" stroke-width="1.3"/><path d="M6 8l6 5 6-5" fill="none" stroke="var(--card-dark)" stroke-width="1.3"/></svg>
        514 555-0178
      </li>
      <li>
        <svg class="contact-icon" viewBox="0 0 24 24"><circle cx="12" cy="12" r="11" fill="var(--ink-light)"/><g fill="none" stroke="var(--card-dark)" stroke-width="1.2"><circle cx="12" cy="12" r="6"/><ellipse cx="12" cy="12" rx="2.6" ry="6"/><path d="M6 12h12"/></g></svg>
        ventdoux514@mail.com
      </li>
    </ul>
    <p class="address">880 Rue Laurier Est<br>Montreal, Quebec H2J0A0</p>
  </div>
</section>

<section class="card card--back">
  <div class="brand">
    <div class="brand-row"><span class="brand-dot"></span><span class="brand-name">Vent doux</span></div>
    <div class="brand-rule"></div>
    <div class="brand-tagline">lunettes &amp; accessoires</div>
  </div>
</section>

</body>
</html>
```